Review/Re-Design Supermarket E-Commerce website

We have launched our Supermarket E-commerce Website but feel it is lacking a modern feel.

Please re-design the current Supermarket E-commerce site, creating a more modern look and feel.

I am looking for design changes to things such as:

- Fonts
- Button shape & Size
- Shapes of boxes
- Layout of drop down menus
- A new shopping cart / button
- The Header (and in particular the use and positioning of the logo)
- Supplying a generic background image (currently berries)

Please do not change the structure of the page. For instance, the category selection will always be on the left, the items will always be displayed in rows of 3 and the shopping cart should be on the right.
Updates

Current site can be found at www.brovanmarket.com.au

Project Deadline Extended
Reason: designs coming in are generally too different from current design. we are looking for less that 10% change to the overall look and feel. one aspect that needs a lot of work is the checkout cart on the right hand side. please checkout http://www2.pelkinfreshmart.com.au/?gclid=QXRP4kdmwnLBHTYEzJuaPGEKtB

Target Market(s)

Consumers buying their weekly grocery shopping online

Industry/Entity Type

Shopping

Number of Pages Required

1 page

Requirements
Must have
• Stick to the branding of the Logo. Which is Red, Blue and White.
• Other colours may be used in small percentages.
Should not have
• Do not change the Structure of the site.

```html
<!DOCTYPE html>
<html lang="en">
<head>
<meta charset="utf-8">
<title>Brovan Market Supermarkets</title>
<link rel="stylesheet" href="https://fonts.googleapis.com/css2?family=Roboto+Condensed:wght@300;400;700&family=Open+Sans:wght@400;600&display=swap">
<style>
:root{
  --red:#e8202e;
  --blue:#0a5eb0;
  --green:#7b9a3a;
  --ink:#333;
  --muted:#666;
  --pink:#f5c3b6;
  --paper:#fff;
  --soft:#f6f6f6;
  --line:#e6e6e6;
  --black:#141414;
}
*{box-sizing:border-box;margin:0;padding:0}
html,body{width:690px;height:1200px;overflow:hidden}
body{background:var(--pink);font-family:"Open Sans",sans-serif;color:var(--ink);position:relative}
.page{position:absolute;left:58px;top:16px;width:575px;height:1172px;background:var(--paper)}

/* header */
.topbar{position:absolute;left:0;top:0;width:575px;height:36px;display:flex;align-items:center;padding:0 16px;font-family:"Roboto Condensed",sans-serif;font-size:8px;font-weight:400;color:var(--ink);white-space:nowrap}
.phone{display:flex;align-items:center;gap:6px}
.phone-icon{width:15px;height:15px;border:1px solid var(--red);border-radius:50%;display:flex;align-items:center;justify-content:center}
.nav{margin-left:auto;display:flex;gap:18px}
.nav span{display:flex;align-items:center;gap:5px}
.nav svg{width:8px;height:8px}
.brand{position:absolute;left:0;top:58px;width:575px;text-align:center;font-family:"Roboto Condensed",sans-serif}
.brand-name{font-size:17px;font-weight:700;color:var(--blue);letter-spacing:.5px;display:inline-flex;align-items:center;gap:7px}
.brand-name i{display:inline-block;width:14px;height:14px;background:var(--red);border-radius:50%}
.brand-sub{font-size:8.5px;font-weight:400;letter-spacing:4px;color:var(--ink);margin-top:1px}

/* hero */
.hero{position:absolute;left:0;top:104px;width:575px;height:341px;background:linear-gradient(135deg,#9b6e4c,#6d4a33 60%,#8a6244)}
.search{position:absolute;left:15px;top:19px;width:546px;height:34px;display:flex}
.search-field{width:274px;background:#fff;display:flex;align-items:center;padding:0 10px;font-size:7.5px;color:var(--red);font-family:"Roboto Condensed",sans-serif;letter-spacing:.3px}
.search-field svg{margin-left:auto}
.filters{flex:1;background:var(--red);display:flex;align-items:center;padding:0 12px;gap:7px;color:#fff;font-family:"Roboto Condensed",sans-serif;font-size:8.5px;white-space:nowrap}
.select{width:82px;height:20px;background:#fff;display:flex;align-items:center;justify-content:flex-end;padding-right:6px;flex:none}
.filters .gap{width:4px}
.slide{position:absolute;left:15px;top:58px;width:546px;height:270px;background:linear-gradient(90deg,#fff 50%,#f1f1f1);overflow:hidden}
.slide h1{position:absolute;left:25px;top:66px;font-family:"Roboto Condensed",sans-serif;font-size:26px;font-weight:700;color:#2c2c2c;letter-spacing:.2px;white-space:nowrap}
.slide h1 em{font-style:normal;color:var(--green)}
.slide h2{position:absolute;left:25px;top:102px;font-family:"Roboto Condensed",sans-serif;font-weight:300;font-size:17px;color:#333}
.slide p{position:absolute;left:25px;top:130px;width:225px;font-size:6px;line-height:10px;color:#555}
.slide-art{position:absolute;left:262px;top:10px;width:270px;height:240px;background:linear-gradient(160deg,#eef0e6,#c9d49a 45%,#c9a06a)}
.price{position:absolute;left:-18px;top:205px;width:155px;height:130px;border-radius:50%/60%;background:var(--green)}
.price span{position:absolute;left:48px;top:25px;color:#fff;font-family:"Roboto Condensed",sans-serif;font-weight:700;font-size:22px}
.shop-now{position:absolute;left:462px;top:190px;width:84px;height:28px;background:var(--red);transform:rotate(-14deg);color:#fff;font-family:"Roboto Condensed",sans-serif;font-weight:700;font-size:13px;display:flex;align-items:center;justify-content:center}

/* categories */
.categories{position:absolute;left:0;top:445px;width:127px;height:592px;padding:26px 0 0 14px}
.col-title{font-family:"Roboto Condensed",sans-serif;font-weight:400;font-size:11px;color:#333;display:flex;align-items:center;gap:6px}
.rule{width:104px;height:1px;background:var(--line);margin-top:7px;position:relative}
.rule:before{content:"";position:absolute;left:0;top:0;width:22px;height:1px;background:var(--red)}
.cat-list{list-style:none;margin-top:13px}
.cat-list li{font-size:6.5px;height:15.8px;line-height:11px;color:#444;display:flex;gap:7px;white-space:nowrap}
.cat-list li:before{content:"»";color:var(--red);font-weight:600}

/* products */
.featured{position:absolute;left:127px;top:445px;width:372px;height:592px;background:var(--soft)}
.featured-head{position:absolute;left:12px;top:22px;font-family:"Roboto Condensed",sans-serif;font-size:12px;color:var(--red)}
.arrows{position:absolute;display:flex;gap:4px}
.arrows b{width:10px;height:10px;border:1px solid #ccc;border-radius:50%;font-size:6px;display:flex;align-items:center;justify-content:center;font-weight:400;color:#555;background:#fff}
.grid{position:absolute;left:10px;top:61px;display:grid;grid-template-columns:repeat(3,94px);column-gap:6px;row-gap:16px}
.card{height:162px;background:#fff;border:1px solid #ececec;padding:8px 8px 0}
.card .shot{height:80px}
.card .name{font-family:"Roboto Condensed",sans-serif;font-weight:400;font-size:7.5px;color:#555;margin-top:14px;white-space:nowrap;overflow:hidden}
.card .cost{font-family:"Roboto Condensed",sans-serif;font-size:8px;color:var(--red);margin-top:7px}
.card .btn{display:inline-block;margin-top:8px;background:var(--red);color:#fff;font-size:7px;padding:4px 7px;border-radius:2px}

/* sidebar */
.sidebar{position:absolute;left:442px;top:445px;width:133px;height:592px;background:var(--soft)}
.collect{height:105px;background:var(--red);color:#fff;padding:24px 10px 0}
.collect .t{font-family:"Roboto Condensed",sans-serif;font-size:10px;display:flex;align-items:center;gap:6px}
.collect .a{font-size:6px;line-height:13px;margin-top:5px}
.collect .t2{margin-top:8px}
.cart{height:84px;background:linear-gradient(135deg,#a3866c,#6f5544);position:relative;color:#fff;text-align:center;font-family:"Roboto Condensed",sans-serif;font-size:9.5px;padding-top:14px;overflow:hidden}
.cart .items{display:flex;align-items:center;justify-content:center;gap:6px}
.cart .sub{margin-top:4px}
.checkout{position:absolute;left:0;bottom:0;width:133px;height:28px;background:var(--red);border-radius:60% 60% 0 0/100% 100% 0 0;font-size:10px;line-height:28px}
.specials{height:191px;position:relative;text-align:center;padding-top:26px}
.specials .t{font-family:"Roboto Condensed",sans-serif;font-size:12px;color:var(--red)}
.specials .art{width:92px;height:96px;margin:12px auto 0;background:linear-gradient(160deg,#f2e3dc,#d3414a 55%,#c7955e)}
.specials .n{font-family:"Roboto Condensed",sans-serif;font-weight:400;font-size:9px;color:#444;margin-top:10px}
.shop-btn{height:22px;background:var(--red);color:#fff;font-family:"Roboto Condensed",sans-serif;font-size:9px;text-align:center;line-height:22px}
.news{padding:12px 10px 0}
.news .col-title{font-size:9.5px}
.news .rule{width:113px}
.news-item{display:flex;gap:7px;margin-top:13px}
.news-item .thumb{width:46px;height:45px;flex:none}
.news-item h4{font-family:"Roboto Condensed",sans-serif;font-weight:400;font-size:8px;color:#333;white-space:nowrap}
.news-item p{font-size:5.5px;line-height:10px;color:#555;margin-top:3px}

/* footer */
.footer{position:absolute;left:0;top:1037px;width:575px;height:99px;background:var(--blue);color:#fff;padding:16px 0 0 22px;display:flex}
.footer h5{font-family:"Roboto Condensed",sans-serif;font-weight:400;font-size:8px;letter-spacing:.2px;white-space:nowrap}
.footer ul{list-style:none;margin-top:10px}
.footer li{font-size:6px;line-height:12px;white-space:nowrap}
.f1{width:97px}.f2{width:92px}.f3{width:97px}.f4{width:124px}
.cards{display:grid;grid-template-columns:repeat(3,25px);gap:5px;margin-top:10px}
.cards span{height:16px;border-radius:2px;background:#fff}
.cards span:nth-child(2){background:#2e7fc9}.cards span:nth-child(4){background:#dce7f3}.cards span:nth-child(5){background:#f0a04b}.cards span:nth-child(6){background:#2a2a2a}
.news-form p{font-size:6px;margin-top:10px}
.news-form .field{width:127px;height:17px;background:#fff;margin-top:6px;color:#888;font-size:5.5px;padding:5px 6px}
.news-form .go{display:inline-block;margin-top:7px;background:var(--red);font-size:6px;font-weight:600;padding:4px 5px}
.bottombar{position:absolute;left:0;top:1136px;width:575px;height:36px;background:var(--black);color:#fff;display:flex;align-items:center;padding:0 19px;font-family:"Roboto Condensed",sans-serif;font-size:6.5px;white-space:nowrap}
.social{margin-left:110px;display:flex;gap:5px}
.social span{width:15px;height:15px;border:1px solid #fff;border-radius:50%}
.legal{margin-left:auto}
</style>
</head>
<body>
<div class="page">
  <header>
    <div class="topbar">
      <div class="phone"><span class="phone-icon"><svg width="8" height="8" viewBox="0 0 24 24"><path d="M6.6 10.8a15 15 0 0 0 6.6 6.6l2.2-2.2c.3-.3.7-.4 1-.2 1.1.4 2.3.6 3.6.6.6 0 1 .4 1 1V20c0 .6-.4 1-1 1A17 17 0 0 1 3 4c0-.6.4-1 1-1h3.5c.6 0 1 .4 1 1 0 1.3.2 2.5.6 3.6.1.3 0 .7-.2 1z" fill="#e8202e"/></svg></span>Phone : 1300 555 019</div>
      <nav class="nav">
        <span><svg viewBox="0 0 10 10"><path d="M0 5 10 0 6 10 5 6z" fill="#e8202e"/></svg>PRODUCTS</span>
        <span><svg viewBox="0 0 10 10"><path d="M0 1h2l1.5 5h5L10 2.5H3" fill="none" stroke="#e8202e" stroke-width="1.4"/><circle cx="4" cy="8.5" r="1" fill="#e8202e"/><circle cx="8" cy="8.5" r="1" fill="#e8202e"/></svg>MY CART</span>
        <span><svg viewBox="0 0 10 10"><rect x="1" y="2" width="7" height="7" fill="none" stroke="#e8202e" stroke-width="1.2"/><path d="M4 6 9 1" stroke="#e8202e" stroke-width="1.4"/></svg>REGISTER</span>
        <span><svg viewBox="0 0 10 10"><rect x="2" y="4.5" width="6" height="5" fill="#e8202e"/><path d="M3.5 4.5V3a1.5 1.5 0 0 1 3 0" fill="none" stroke="#e8202e" stroke-width="1.2"/></svg>LOGIN</span>
      </nav>
    </div>
    <div class="brand">
      <div class="brand-name">BROVAN MARKET<i></i></div>
      <div class="brand-sub">SUPERMARKETS</div>
    </div>
  </header>

  <section class="hero" role="img" aria-label="Rustic wooden table backdrop">
    <div class="search">
      <div class="search-field">SEARCH<svg width="9" height="9" viewBox="0 0 10 10"><circle cx="4" cy="4" r="3" fill="none" stroke="#444" stroke-width="1.3"/><path d="M6.3 6.3 9 9" stroke="#444" stroke-width="1.5"/></svg></div>
      <div class="filters">FILTER BY<span class="select"><svg width="5" height="5" viewBox="0 0 10 10"><path d="M1 2l4 3 4-3M1 6l4 3 4-3" fill="none" stroke="#777" stroke-width="1.3"/></svg></span><span class="gap"></span>SORT<span class="select"><svg width="5" height="5" viewBox="0 0 10 10"><path d="M1 2l4 3 4-3M1 6l4 3 4-3" fill="none" stroke="#777" stroke-width="1.3"/></svg></span></div>
    </div>
    <div class="slide">
      <h1>APPLES <em>NUTRITION</em></h1>
      <h2>Online Specials</h2>
      <p>Nam elit agna,endrerit sit amet, tincidunt ac, viverra sed, nulla. Donec porta diam eu massa. Quisque diam lorem, interdum vitae, dapibus</p>
      <div class="slide-art" role="img" aria-label="Photo: wicker basket of green apples with loose apples beside it"></div>
      <div class="price"><span>$13.00</span></div>
      <div class="shop-now">Shop Now!</div>
    </div>
  </section>

  <aside class="categories">
    <div class="col-title"><svg width="9" height="9" viewBox="0 0 10 10"><path d="M1 4h2v5H1zM3 4l3-3c1 0 1 1 .8 2H9v2l-1.5 4H3" fill="none" stroke="#555" stroke-width="1"/></svg>CATEGORIES</div>
    <div class="rule"></div>
    <ul class="cat-list">
      <li>Baby</li><li>Accessories</li><li>Bakery</li><li>Baking Needs</li><li>Beverages</li><li>Biscuits</li><li>Breakfast Foods</li><li>Cereal</li><li>Canned Food</li><li>Cheese</li><li>Chilled Foods</li><li>Chips</li><li>Condiments</li><li>Confectionery</li><li>Cooking Needs, Seasoning</li><li>Desserts</li><li>Frozen Food</li><li>Fruit</li><li>Hardware &amp; Outdoor</li><li>Health Foods</li><li>Homewares</li><li>Household Cleaning</li><li>International Foods</li><li>Jams &amp; Spreads</li><li>Laundry</li><li>Meat</li><li>Milk</li><li>Packet Food</li><li>Pet Care</li><li>Serviced Deli</li><li>Snacks</li><li>Soft Drinks</li><li>Tissue Products</li>
    </ul>
  </aside>

  <main class="featured">
    <div class="featured-head">Featured Products</div>
    <div class="arrows" style="left:337px;top:23px"><b>‹</b><b>›</b></div>
    <div class="grid">
      <div class="card"><div class="shot" role="img" aria-label="Product photo: red apples" style="background:linear-gradient(180deg,#fff,#e9b3b5 50%,#fff)"></div><div class="name">Apples Red 2kg Bag</div><div class="cost">$56.00</div><span class="btn">Add to Cart</span></div>
      <div class="card"><div class="shot" role="img" aria-label="Product photo: red apple" style="background:linear-gradient(180deg,#fff,#e7bdb5 50%,#fff)"></div><div class="name">Apples Red 2kg Bag</div><div class="cost">$56.00</div><span class="btn">Add to Cart</span></div>
      <div class="card"><div class="shot" role="img" aria-label="Product photo: green apple" style="background:linear-gradient(180deg,#fff,#c5e5ac 50%,#fff)"></div><div class="name">Apples Red 2kg Bag</div><div class="cost">$56.00</div><span class="btn">Add to Cart</span></div>
      <div class="card"><div class="shot" role="img" aria-label="Product photo: green apples" style="background:linear-gradient(180deg,#fff,#dbe7b4 50%,#fff)"></div><div class="name">Apples Red 2kg Bag</div><div class="cost">$56.00</div><span class="btn">Add to Cart</span></div>
      <div class="card"><div class="shot" role="img" aria-label="Product photo: tin of instant coffee" style="background:linear-gradient(180deg,#fff,#c7b8b2 50%,#fff)"></div><div class="name">Kerro Blend 27 Coffee</div><div class="cost">$56.00</div><span class="btn">Add to Cart</span></div>
      <div class="card"><div class="shot" role="img" aria-label="Product photo: bottle of laundry liquid" style="background:linear-gradient(180deg,#fff,#b7c8ea 50%,#fff)"></div><div class="name">Zento Ultra Laundry</div><div class="cost">$56.00</div><span class="btn">Add to Cart</span></div>
      <div class="card"><div class="shot" role="img" aria-label="Product photo: bag of dry dog food, beef" style="background:linear-gradient(180deg,#fff,#e4b6b7 50%,#fff)"></div><div class="name">Rufus Crunchy Beef</div><div class="cost">$56.00</div><span class="btn">Add to Cart</span></div>
      <div class="card"><div class="shot" role="img" aria-label="Product photo: bag of dry dog food, chicken" style="background:linear-gradient(180deg,#fff,#efe2a6 50%,#fff)"></div><div class="name">Rufus Crunchy Chicken</div><div class="cost">$56.00</div><span class="btn">Add to Cart</span></div>
      <div class="card"><div class="shot" role="img" aria-label="Product photo: packaged fruit loaf" style="background:linear-gradient(180deg,#fff,#ddd2c8 50%,#fff)"></div><div class="name">Hollins Bake Fruit</div><div class="cost">$56.00</div><span class="btn">Add to Cart</span></div>
    </div>
  </main>

  <aside class="sidebar">
    <div class="collect">
      <div class="t"><svg width="8" height="8" viewBox="0 0 10 10"><path d="M0 5 10 0 6 10 5 6z" fill="#fff"/></svg>Click &amp; Collect</div>
      <div class="a">4/12-18 MARLOW ST KENTSFORD<br>TAS 7290</div>
      <div class="t t2"><svg width="8" height="9" viewBox="0 0 10 11"><rect x="1" y="0" width="8" height="8" rx="2" fill="#fff"/><rect x="2" y="2" width="6" height="3" fill="#e8202e"/><circle cx="3" cy="9.5" r="1" fill="#fff"/><circle cx="7" cy="9.5" r="1" fill="#fff"/></svg>Delivery Info</div>
    </div>
    <div class="cart" role="img" aria-label="Shopping cart summary over a soft grocery backdrop">
      <div class="items"><svg width="11" height="9" viewBox="0 0 11 9"><path d="M0 .8h2l1.3 5h5.5L10.5 2H3" fill="#fff" stroke="#fff"/><circle cx="4" cy="8" r="1" fill="#fff"/><circle cx="8.5" cy="8" r="1" fill="#fff"/></svg>0 items</div>
      <div class="sub">Sub Total $0.00</div>
      <div class="checkout">CHECKOUT</div>
    </div>
    <div class="specials">
      <div class="arrows" style="left:18px;top:28px"><b>‹</b></div>
      <div class="arrows" style="left:105px;top:28px"><b>›</b></div>
      <div class="t">SPECIALS</div>
      <div class="art" role="img" aria-label="Photo: basket of red cherries"></div>
      <div class="n">Nanking Cherry</div>
    </div>
    <div class="shop-btn">SHOP NOW</div>
    <div class="news">
      <div class="col-title"><svg width="8" height="8" viewBox="0 0 10 10"><rect x=".5" y="1.5" width="9" height="8" fill="none" stroke="#555"/><path d="M.5 4h9" stroke="#555"/></svg>Latest News</div>
      <div class="rule"></div>
      <div class="news-item"><div class="thumb" role="img" aria-label="Photo: cherries on a branch" style="background:linear-gradient(135deg,#6e8f3a,#b8212b)"></div><div><h4>Sed ut perspiciatis</h4><p>Lorem ipsum dolor sit amet, consectetur adipiscing elit.</p></div></div>
      <div class="news-item"><div class="thumb" role="img" aria-label="Photo: fruit harvest in the orchard" style="background:linear-gradient(135deg,#4a6a2a,#9a5a3a)"></div><div><h4>Sed ut perspiciatis</h4><p>Lorem ipsum dolor sit amet, consectetur adipiscing elit.</p></div></div>
    </div>
  </aside>

  <footer class="footer">
    <div class="f1"><h5>INFORMATION</h5><ul><li>Terms of Use</li><li>Privacy Policy</li><li>Returns Policy</li><li>Security Policy</li></ul></div>
    <div class="f2"><h5>ABOUT US</h5><ul><li>About Us</li><li>Company Blog</li><li>Contact Us</li></ul></div>
    <div class="f3"><h5>MY ACCOUNT</h5><ul><li>My Account</li><li>My Past Orders</li><li>Online Specials</li><li>Everyday Specials</li></ul></div>
    <div class="f4"><h5>MAKE A PAYMENT</h5><div class="cards"><span></span><span></span><span></span><span></span><span></span><span></span></div></div>
    <div class="news-form"><h5>STAY IN TOUCH</h5><p>Subscribe to our newsletter :</p><div class="field">Enter Your Email</div><span class="go">SUBSCRIBE</span></div>
  </footer>
  <div class="bottombar">
    <span>©2014 - 2015 BROVAN MARKET. ALL RIGHTS RESERVED.</span>
    <div class="social"><span></span><span></span><span></span><span></span><span></span></div>
    <span class="legal">PRIVACY NOTICE &nbsp;|&nbsp; CONDITIONS OF USE</span>
  </div>
</div>
</body>
</html>
```